Large scale additive manufacturing system brochure

Project Title: ZORIL Series THERMOPLASTIC EXTRUDER– Product Catalog Design

Description:
We need a professional catalog design for our ZORIL Series extruders (ZORIL15, ZORIL20, ZORIL32), which are high-performance extrusion systems for large-scale thermoplastic 3D printing. The catalog should highlight technical specifications, key features, applications, and company profile.

Requirements:
• Clean and modern layout aligned with Brimtel corporate colors
• 10–12 pages including cover, product comparison tables, technical details, and application visuals
• Output capacities should be presented based on PETG +30% GF benchmark
• Integration of company’s partnerships (TOLMI, OBRU, Qe Forge, Movrel)
• Space for product renders, real application images, and technical drawings
• English text will be provided, but layout and professional design are required

Deliverables:
• Editable source file (InDesign / Illustrator / similar)
• Print-ready PDF version

*i upload the previous catalog, which doesn’t show our vision abd future aim. We need a professional, unique and impressive design.

Target Market(s)

Defense, aerospace, marine, furniture, composite manufacturing

Industry/Entity Type

Robotics and automation

Font styles to use
Sans Serif

Colors

Designer to choose colors to be used in the design.

Requirements
Must have
• High tech impressive view
Nice to have
• Must seen a unique high tech product catalog

```html
<!DOCTYPE html>
<html lang="en">
<head>
<meta charset="utf-8">
<title>ZORIL Series – Product Catalog Spreads</title>
<link href="https://fonts.googleapis.com/css2?family=Exo+2:ital,wght@0,600;0,700;0,800;1,600;1,700;1,800&family=Montserrat:wght@400;500;600;700&display=swap" rel="stylesheet">
<style>
:root{
  --orange:#f39314;
  --orange-dark:#a85a05;
  --ink:#1d1d1d;
  --text:#2f2f2f;
  --muted:#666;
  --rule:#d4d4d4;
  --canvas:#e7e7e7;
  --panel:#f1f1f1;
  --white:#fff;
}
*{margin:0;padding:0;box-sizing:border-box}
html,body{width:1200px;height:849px;overflow:hidden;background:var(--canvas)}
body{position:relative;font-family:"Montserrat",sans-serif;color:var(--text)}
.spread{position:absolute;width:360px;height:254px;background:var(--white);overflow:hidden}
.a{position:absolute}
.h{font-family:"Exo 2",sans-serif;font-weight:800;color:var(--orange);line-height:1}
.h.u{border-bottom:.7px solid var(--orange);padding-bottom:1px;display:inline-block}
.p{font-size:2.6px;line-height:1.4;color:var(--text);font-weight:500}
.p b{color:var(--ink);font-weight:700}
.photo{background:linear-gradient(135deg,#a3a5a8,#6b6f73 55%,#45484b)}
.photo.warm{background:linear-gradient(140deg,#d6d6d6,#a98567 45%,#d9782e 70%,#555)}
.photo.light{background:linear-gradient(160deg,#f6f6f6,#dcdddf 60%,#b9bbbe)}
.photo.dark{background:linear-gradient(150deg,#5a5d62,#2a2c2f)}
.hex{clip-path:polygon(25% 0,75% 0,100% 50%,75% 100%,25% 100%,0 50%)}
.cut{clip-path:polygon(0 0,88% 0,100% 12%,100% 100%,12% 100%,0 88%)}
.foot{position:absolute;left:0;right:0;bottom:0;height:12px;background:var(--ink);clip-path:polygon(1.5% 0,98.5% 0,100% 100%,0 100%)}
.brand{position:absolute;display:flex;align-items:center;gap:2px;font-family:"Montserrat",sans-serif;font-weight:700;letter-spacing:.8px;color:var(--orange);font-size:4px}
.brand i{display:block;width:5px;height:5px;border-radius:50%;border:.6px solid var(--orange)}
.foot .brand{left:12px;top:3.5px}
.tag{position:absolute;background:var(--orange);color:var(--white);font-family:"Exo 2",sans-serif;font-weight:800;text-align:center;clip-path:polygon(6% 0,100% 0,94% 100%,0 100%)}
.tbl{position:absolute;display:grid;font-size:2.5px;line-height:1.35;color:var(--text);font-weight:500}
.tbl .th{color:var(--orange);font-weight:700}
.tbl>div{padding:1.5px 1px;border-bottom:.3px solid var(--rule)}
.list{font-size:2.45px;line-height:1.38;color:var(--text);list-style:none;font-weight:500}
.list li{margin-bottom:2.2px;padding-left:2.2px;position:relative}
.list li::before{content:"";position:absolute;left:0;top:1px;width:.9px;height:.9px;background:var(--orange)}
.list b{color:var(--ink);font-weight:700}
.sub{font-size:2.7px;font-weight:700;color:var(--ink);text-align:center;margin:2.5px 0 2px}
.col-rule{position:absolute;width:.3px;background:var(--rule)}
.feat{display:flex;gap:3px;align-items:center;margin-bottom:4px;font-size:2.5px}
</style>
</head>
<body>

<!-- ===== Cover spread ===== -->
<section class="spread" style="left:218px;top:29px">
  <div class="a" style="left:0;top:0;width:180px;height:254px;background:var(--orange)"></div>
  <div class="brand" style="left:34px;top:104px;color:var(--orange-dark);font-size:21px;letter-spacing:3px;gap:6px"><i style="border:2px solid var(--orange-dark);width:18px;height:18px"></i>BRIMTEL</div>
  <div class="a" style="left:38px;top:204px;font-size:3.6px;font-weight:700;color:#6e3b00">CONTACT</div>
  <div class="a p" style="left:38px;top:210px;font-size:2.6px;color:#7d4303;line-height:1.5"><b style="color:#6e3b00">Brimtel Robotics &amp; Automation</b><br>Northport – HQ &amp; Production<br>Eastbay – Office &amp; Workshop</div>
  <div class="a p" style="left:106px;top:209px;font-size:2.6px;color:#7d4303;line-height:1.6">◦ Brimtel Robotics<br>✉ info@brimtel.example<br>⊕ www.brimtel.example</div>

  <div class="a photo light" style="left:180px;top:0;width:180px;height:166px" role="img" aria-label="Orange industrial robot arm with extruder printing a large white part"></div>
  <div class="a" style="left:180px;top:150px;width:180px;height:70px;background:var(--ink);clip-path:polygon(0 22%,52% 22%,68% 0,100% 0,100% 100%,0 100%)"></div>
  <div class="a h" style="left:203px;top:177px;font-size:10px;font-style:italic">ZORIL Series</div>
  <div class="a" style="left:203px;top:189px;font-family:'Exo 2',sans-serif;font-style:italic;font-weight:600;font-size:5.8px;color:var(--orange)">– High-Performance</div>
  <div class="a" style="left:203px;top:198px;font-family:'Exo 2',sans-serif;font-style:italic;font-weight:600;font-size:4.6px;line-height:1.35;color:var(--white)">Extruders for Large-Scale<br>Thermoplastic 3D Printing</div>
  <div class="brand" style="left:203px;top:234px;color:var(--ink);font-size:6px;letter-spacing:1.4px"><i style="border-color:var(--ink);width:7px;height:7px"></i>BRIMTEL</div>
</section>

<!-- ===== Summary / overview spread ===== -->
<section class="spread" style="left:621px;top:29px">
  <div class="a" style="left:0;top:0;width:86px;height:81px;background:var(--orange)"></div>
  <div class="a h u" style="left:12px;top:17px;font-size:5.6px;color:var(--white);border-color:var(--white)">Executive Summary</div>
  <div class="a p" style="left:12px;top:27px;width:64px;font-size:2.5px;color:#fff7ea">The ZORIL Series (ZORIL15, ZORIL20, ZORIL32) comprises industrial extruders for large-scale thermoplastic 3D printing. Benchmarked with PETG +30% GF, ZORIL delivers reliable output up to 40 kg/h at up to 450 °C. As an official TOLMI System Partner and partner of OBRU, Qe Forge and Movrel, Brimtel joins robust hardware with robotic CAM and AI-driven optimization.</div>
  <div class="a" style="left:13px;top:94px;font-size:4px;font-weight:700;color:var(--orange)">TOLMI</div>
  <div class="a p" style="left:37px;top:93px;font-size:2.3px;color:var(--muted);border-left:.3px solid var(--muted);padding-left:2px;line-height:1.3">Official System<br>Partner</div>
  <div class="a" style="left:13px;top:105px;font-size:4px;font-weight:700;color:var(--orange)">OBRU</div>
  <div class="a p" style="left:36px;top:106px;font-size:2.3px;color:var(--ink)">Go beyond CAD/CAM</div>
  <div class="a photo light" style="left:0;top:128px;width:86px;height:102px" role="img" aria-label="Robot arm beside pellet extruder and control cabinet on a slider"></div>

  <div class="a h u" style="left:97px;top:17px;font-size:5.6px">About Brimtel</div>
  <div class="a p" style="left:97px;top:27px;width:62px;font-size:2.45px">Brimtel Robotics &amp; Automation is a global engineering company specializing in robotic systems for additive manufacturing, milling, and automation. With exports to 40+ countries across 6 continents, Brimtel serves construction, marine, automotive, and manufacturing. Partners: TOLMI, OBRU, Qe Forge, and Movrel.</div>
  <div class="a h" style="left:97px;top:76px;font-size:5.6px">Sectors Served</div>
  <div class="a p" style="left:97px;top:86px;width:62px;font-size:2.4px;line-height:1.35">
    <b>DEFENSE:</b> rapid prototyping of housings, low-volume tooling, jigs &amp; fixtures, composite mold masters.<br><br>
    <b>AEROSPACE:</b> layup tools, vacuum form tools, drill jigs, aerodynamic mockups.<br><br>
    <b>MARINE:</b> hull sections, fairings, cores, custom molds, corrosion-resistant parts.<br><br>
    <b>FURNITURE:</b> sculptural shells, ergonomic forms, upholstery molds.<br><br>
    <b>INTERIOR DESIGN:</b> parametric panels, bespoke décor, lighting housings.<br><br>
    <b>AUTOMOTIVE:</b> prototype body panels, bumpers, fixtures, assembly aids.<br><br>
    <b>CONSTRUCTION/ARCHITECTURE:</b> façade panels, casting molds, large functional parts.
  </div>

  <div class="a h" style="left:195px;top:25px;font-size:7px;width:150px;text-align:center">ZORIL Series Overview</div>
  <div class="a p" style="left:192px;top:35px;width:156px;font-size:2.4px;text-align:center">ZORIL extruders are built for continuous, high-throughput production of large-format parts in reinforced thermoplastics, with multi-zone heating and robotic interfaces.</div>
  <div class="tbl" style="left:192px;top:50px;width:156px;grid-template-columns:24px 20px 32px 20px 36px 24px">
    <div class="th">Model</div><div class="th">Screw Diameter</div><div class="th">Output (PETG +30% GF)</div><div class="th">Heating Zones</div><div class="th">Max Temperature</div><div class="th">Primary Use</div>
    <div style="height:21px">ZORIL15</div><div>25 mm</div><div>15 kg/h</div><div>4</div><div>450 °C universities, mid-size prototypes</div><div>R&amp;D labs</div>
    <div style="height:21px">ZORIL20</div><div>25 mm</div><div>20 kg/h</div><div>4</div><div>450 °C prototyping, tooling &amp; molds</div><div>Industrial</div>
    <div style="height:21px">ZORIL32</div><div>35 mm</div><div>40 kg/h</div><div>4</div><div>450 °C production, large structural parts</div><div>Heavy-duty</div>
  </div>

  <div class="tag" style="left:192px;top:138px;width:46px;height:7px;font-size:4.2px;line-height:7px">ZORIL15</div>
  <div class="tag" style="left:246px;top:138px;width:46px;height:7px;font-size:4.2px;line-height:7px">ZORIL20</div>
  <div class="tag" style="left:300px;top:138px;width:46px;height:7px;font-size:4.2px;line-height:7px">ZORIL32</div>
  <div class="col-rule" style="left:242px;top:148px;height:86px"></div>
  <div class="col-rule" style="left:296px;top:148px;height:86px"></div>
  <div class="a" style="left:192px;top:148px;width:47px">
    <div class="p" style="font-size:2.4px">25 mm screw, 4 heating zones, max 450 °C. Delivers up to 15 kg/h (PETG +30% GF) with repeatable output.</div>
    <div class="sub">HIGHLIGHTS:</div>
    <ul class="list"><li>Compact footprint with industrial reliability for labs and pilot lines.</li><li>Ideal for mid-size parts and materials R&amp;D.</li><li>Quick-change nozzle and service-friendly layout.</li></ul>
  </div>
  <div class="a" style="left:246px;top:148px;width:47px">
    <div class="p" style="font-size:2.4px">25 mm screw, 4 heating zones, max 450 °C. Delivers up to 20 kg/h (PETG +30% GF) with repeatable output.</div>
    <div class="sub">HIGHLIGHTS:</div>
    <ul class="list"><li>Workhorse extruder for industrial prototyping and tooling.</li><li>Balanced throughput vs. footprint for factories.</li><li>Proven with GF-reinforced filaments and pellets.</li></ul>
  </div>
  <div class="a" style="left:300px;top:148px;width:47px">
    <div class="p" style="font-size:2.4px">35 mm screw, 4 heating zones, max 450 °C. Delivers up to 40 kg/h (PETG +30% GF) with repeatable output.</div>
    <div class="sub">HIGHLIGHTS:</div>
    <ul class="list"><li>High-throughput system for heavy-duty production.</li><li>Stable melt quality at high flow rates.</li><li>Built for continuous runs with reinforced polymers.</li></ul>
  </div>
  <div class="foot"><div class="brand"><i></i>BRIMTEL</div></div>
</section>

<!-- ===== Materials spread ===== -->
<section class="spread" style="left:218px;top:297px">
  <div class="a photo warm cut" style="left:0;top:17px;width:167px;height:212px" role="img" aria-label="Orange robot on tracked base beside a tall printed grey column at an exhibition stand"></div>
  <div class="a h u" style="left:199px;top:49px;font-size:7px">Materials &amp; Process Guidelines (Typical)</div>
  <div class="a p" style="left:192px;top:62px;width:152px;font-size:2.45px;text-align:center">The following ranges are indicative; exact parameters depend on polymer grade, filler percentage, and part geometry. Benchmarking is recommended for each application.</div>
  <div class="tbl" style="left:192px;top:77px;width:154px;grid-template-columns:30px 28px 28px 28px 40px">
    <div class="th">Material</div><div class="th">Typical Nozzle Ø</div><div class="th">Layer Height</div><div class="th">Melt Temp Window</div><div class="th">Notes</div>
    <div style="height:31px">PETG +30% GF (reference)</div><div>1.5–6.0 mm</div><div>30–60% of nozzle Ø</div><div>250–300 °C</div><div>Reference material for ZORIL throughput; good dimensional stability.</div>
    <div style="height:31px">PP +20–30% GF</div><div>1.5–6.0 mm</div><div>30–60% of nozzle Ø</div><div>220–260 °C</div><div>Lightweight with chemical resistance; shrinkage control needed.</div>
    <div style="height:27px">PA6/PA12 + GF/CF</div><div>1.5–6.0 mm</div><div>30–50% of nozzle Ø</div><div>260–320 °C</div><div>High strength; moisture control and enclosure advised.</div>
    <div style="height:27px">PC / PC blends</div><div>1.5–6.0 mm</div><div>30–50% of nozzle Ø</div><div>280–320 °C</div><div>High heat deflection; enclosure improves adhesion.</div>
    <div style="height:22px;border:0">ABS / ASA (reinforced)</div><div style="border:0">1.5–6.0 mm</div><div style="border:0">30–50% of nozzle Ø</div><div style="border:0">240–270 °C</div><div style="border:0">General-purpose; ASA has better UV stability.</div>
  </div>
  <div class="foot"><div class="brand"><i></i>BRIMTEL</div></div>
</section>

<!-- ===== Robotic printers spread ===== -->
<section class="spread" style="left:621px;top:297px">
  <div class="a photo cut" style="left:12px;top:17px;width:155px;height:99px" role="img" aria-label="Close view of extruder head mounted on robot arm"></div>
  <div class="tag" style="left:16px;top:29px;width:86px;height:9px;font-size:6px;line-height:9px">ROBOTIC PRINTERS</div>
  <div class="a photo dark cut" style="left:192px;top:17px;width:156px;height:99px" role="img" aria-label="Large printed boat hull displayed at a trade fair with visitors"></div>

  <div class="a h" style="left:25px;top:124px;font-size:7px">ZORIL Series</div>
  <div class="a p" style="left:25px;top:133px;font-size:2.5px;width:46px">Next Generation Thermoplastic 3D Printers</div>
  <div class="a" style="left:25px;top:146px;width:44px">
    <div class="p feat"><svg width="7" height="9" viewBox="0 0 7 9"><rect x="2.5" y="0.5" width="2" height="6" rx="1" fill="none" stroke="#555" stroke-width=".5"/><circle cx="3.5" cy="7" r="1.5" fill="#555"/></svg><span>450°C Max Temperature</span></div>
    <div class="p feat"><svg width="7" height="7" viewBox="0 0 7 7"><rect x=".5" y=".5" width="6" height="6" fill="none" stroke="#555" stroke-width=".5"/><path d="M2 5V3M3.5 5V2M5 5V4" stroke="#555" stroke-width=".5"/></svg><span>High Productivity With GF/CF Polymers</span></div>
    <div class="p feat"><svg width="7" height="7" viewBox="0 0 7 7"><circle cx="3.5" cy="3.5" r="3" fill="none" stroke="#555" stroke-width=".5"/><path d="M3.5 1.5v2h1.5" stroke="#555" stroke-width=".5" fill="none"/></svg><span>Long-Term Operation</span></div>
    <div class="p feat"><svg width="7" height="7" viewBox="0 0 7 7"><path d="M.5 6.5h6M.5 6.5L6 1" stroke="#555" stroke-width=".5" fill="none"/></svg><span>Multi Angular Printing</span></div>
    <div class="p feat"><svg width="7" height="7" viewBox="0 0 7 7"><circle cx="3.5" cy="3.5" r="3" fill="#bbb"/></svg><span>Complex Structures</span></div>
  </div>
  <div class="a photo light" style="left:76px;top:135px;width:16px;height:68px" role="img" aria-label="ZORIL10 extruder render"></div>
  <div class="a photo light" style="left:111px;top:135px;width:16px;height:68px" role="img" aria-label="ZORIL20 extruder render"></div>
  <div class="a" style="left:146px;top:135px;width:16px;height:68px;background:linear-gradient(160deg,#f4f4f4,#c3c9dc 60%,#9aa0b6)" role="img" aria-label="ZORIL32 extruder render"></div>
  <div class="tag" style="left:69px;top:207px;width:28px;height:6.5px;font-size:3.8px;line-height:6.5px">ZORIL10</div>
  <div class="tag" style="left:104px;top:207px;width:28px;height:6.5px;font-size:3.8px;line-height:6.5px">ZORIL20</div>
  <div class="tag" style="left:139px;top:207px;width:28px;height:6.5px;font-size:3.8px;line-height:6.5px">ZORIL32</div>

  <div class="tag" style="left:192px;top:124px;width:46px;height:11px;font-size:3.8px;line-height:1.2;padding-top:1px">Software &amp;<br>Workflow</div>
  <div class="tag" style="left:246px;top:124px;width:46px;height:11px;font-size:3.8px;line-height:1.2;padding-top:1px">Integration<br>&amp; Interfaces</div>
  <div class="tag" style="left:300px;top:124px;width:46px;height:11px;font-size:3.8px;line-height:1.2;padding-top:1px">Quality, Reliability<br>&amp; Compliance</div>
  <div class="col-rule" style="left:242px;top:138px;height:90px"></div>
  <div class="col-rule" style="left:296px;top:138px;height:90px"></div>
  <ul class="list a" style="left:192px;top:139px;width:47px"><li>CAD/CAM pathing with OBRU: robotic toolpaths, bead width and layer height.</li><li>AI optimization with Qe Forge: simulate and validate paths to reduce defects.</li><li>Robotic additive with Movrel: programming, calibration and multi-axis cells.</li><li>Closed-loop practice: optional temperature, flow and vision sensors.</li></ul>
  <ul class="list a" style="left:246px;top:139px;width:47px"><li>Robotic platforms: validated with TOLMI, Vantor and Keldra robots.</li><li>Mounting: flange mounting; hole patterns in technical drawings.</li><li>Controls: standard robot signaling, digital I/O and native interfaces.</li><li>Cooling: water-cooled barrel and nozzle for thermal stability.</li><li>Safety: interlocks and temperature protections per best practice.</li></ul>
  <ul class="list a" style="left:300px;top:139px;width:47px"><li>Continuous operation proven in long-duration production.</li><li>Design follows CE principles; risk assessment and documents on request.</li><li>Factory (FAT) and site (SAT) acceptance test procedures available.</li></ul>
  <div class="foot"><div class="brand"><i></i>BRIMTEL</div></div>
</section>

<!-- ===== Raw materials spread ===== -->
<section class="spread" style="left:218px;top:565px">
  <div class="a" style="left:0;top:0;width:85px;height:242px;background:var(--panel)"></div>
  <div class="a h u" style="left:101px;top:14px;font-size:7px">RAW MATERIALS</div>
  <div class="a photo light" style="left:15px;top:27px;width:92px;height:58px" role="img" aria-label="Robot arm printing a white part on a slider table"></div>
  <div class="a photo dark" style="left:112px;top:33px;width:52px;height:45px" role="img" aria-label="Black printed lounge chair"></div>
  <div class="a photo dark" style="left:15px;top:112px;width:92px;height:52px" role="img" aria-label="Set of black printed chairs and table"></div>
  <div class="a" style="left:110px;top:97px;width:56px;height:68px;background:linear-gradient(135deg,#f6e0c2,#f39314 50%,#fbeedd)" role="img" aria-label="Printed chair with orange and white striped layers"></div>
  <div class="a h u" style="left:101px;top:168px;font-size:5.6px">Accessories &amp; Options</div>
  <ul class="list a" style="left:101px;top:178px;width:70px"><li><b>NOZZLES:</b> multiple diameters for varying bead widths and deposition rates.</li><li><b>MATERIAL HANDLING:</b> hopper and dryer integration for reinforced pellets.</li><li><b>CALIBRATION AIDS:</b> alignment gauges and flow calibration routines.</li><li><b>ENCLOSURES &amp; SHIELDS:</b> thermal and safety enclosures where required.</li></ul>

  <div class="a photo hex" style="left:193px;top:55px;width:48px;height:43px" role="img" aria-label="Robot teach pendant screen"></div>
  <div class="a photo warm hex" style="left:244px;top:55px;width:48px;height:43px" role="img" aria-label="Technician at printing cell"></div>
  <div class="a photo light hex" style="left:295px;top:55px;width:48px;height:43px" role="img" aria-label="Robot with extruder head during setup"></div>
  <div class="a h u" style="left:202px;top:105px;font-size:6.4px">Installation, Commissioning &amp; Training</div>
  <div class="a p" style="left:192px;top:117px;width:154px;font-size:2.45px;text-align:center">Brimtel provides commissioning support, operator training, and process tuning. The on-site package covers mechanical mounting, parameter setup for PETG +30% GF, and workflow handover with OBRU, Qe Forge, and Movrel toolchains.</div>
  <div class="a" style="left:180px;top:145px;width:180px;height:97px;background:var(--panel)"></div>
  <div class="tag" style="left:193px;top:157px;width:46px;height:11px;font-size:3.8px;line-height:1.2;padding-top:1px">Support<br>&amp; Service</div>
  <div class="tag" style="left:247px;top:157px;width:46px;height:11px;font-size:3.8px;line-height:1.2;padding-top:1px">ROI &amp;<br>Business Impact</div>
  <div class="tag" style="left:301px;top:157px;width:46px;height:11px;font-size:3.8px;line-height:1.2;padding-top:1px">Ordering<br>Information</div>
  <div class="col-rule" style="left:243px;top:171px;height:64px"></div>
  <div class="col-rule" style="left:297px;top:171px;height:64px"></div>
  <ul class="list a" style="left:193px;top:172px;width:47px"><li>1-year free technical support with every ZORIL extruder.</li><li>Advanced subscription: remote support, site visits and process audits.</li><li>Spare parts &amp; preventive maintenance available globally.</li></ul>
  <ul class="list a" style="left:247px;top:172px;width:47px"><li>Cut lead times for large tooling from weeks to days.</li><li>Lower material waste through targeted deposition.</li><li>Design freedom for light, high-strength parts.</li><li>ZORIL32 for production; ZORIL15/20 for development.</li></ul>
  <ul class="list a" style="left:301px;top:172px;width:47px"><li>Select model (ZORIL15 / 20 / 32) by throughput and part scale.</li><li>Confirm material set and nozzle assortment.</li><li>Define integration scope with the robot platform.</li><li>Optional: support subscription and training.</li></ul>
  <div class="foot"><div class="brand"><i></i>BRIMTEL</div></div>
</section>

<!-- ===== Design spread ===== -->
<section class="spread" style="left:621px;top:565px">
  <div class="a cut" style="left:0;top:17px;width:164px;height:212px;background:linear-gradient(150deg,#dedede,#a8a8a8 40%,#6c6c6c 70%,#d47a2a)" role="img" aria-label="Engineer adjusting the nozzle of a ZORIL extruder"></div>
  <div class="a h u" style="left:205px;top:16px;font-size:7px">DESIGN</div>
  <div class="a photo light" style="left:206px;top:28px;width:142px;height:116px;background:linear-gradient(170deg,#fff,#f2f2f2 40%,#d6d6d6)" role="img" aria-label="System layout: robot on slider, extruder, dryer, control panel and printing table"></div>
  <div class="tag" style="left:230px;top:54px;width:7px;height:5.5px;font-size:3.4px;line-height:5.5px">1</div>
  <div class="tag" style="left:290px;top:33px;width:7px;height:5.5px;font-size:3.4px;line-height:5.5px">2</div>
  <div class="tag" style="left:328px;top:79px;width:7px;height:5.5px;font-size:3.4px;line-height:5.5px">3</div>
  <div class="tag" style="left:275px;top:85px;width:7px;height:5.5px;font-size:3.4px;line-height:5.5px">4</div>
  <div class="tag" style="left:333px;top:115px;width:7px;height:5.5px;font-size:3.4px;line-height:5.5px">5</div>
  <div class="tag" style="left:263px;top:108px;width:7px;height:5.5px;font-size:3.4px;line-height:5.5px">6</div>
  <div class="a p" style="left:204px;top:147px;font-size:3.1px;line-height:1.5">1.&nbsp; TOLMI Robot<br>2.&nbsp; ZORIL Series</div>
  <div class="a p" style="left:253px;top:147px;font-size:3.1px;line-height:1.5">3.&nbsp; Dryer<br>4.&nbsp; Control Panel</div>
  <div class="a p" style="left:302px;top:147px;font-size:3.1px;line-height:1.5">5.&nbsp; Printing Table<br>6.&nbsp; Slider (3-30 M)</div>
  <div class="a hex" style="left:193px;top:158px;width:46px;height:40px;background:linear-gradient(150deg,#3f5d8c,#232a3a)" role="img" aria-label="CAM software screen"></div>
  <div class="a photo light hex" style="left:247px;top:158px;width:46px;height:40px" role="img" aria-label="Printing cell in operation"></div>
  <div class="a photo warm hex" style="left:301px;top:158px;width:46px;height:40px" role="img" aria-label="Technician providing service on extruder"></div>
  <div class="tag" style="left:199px;top:198px;width:34px;height:6px;font-size:3.6px;line-height:6px">CAM</div>
  <div class="tag" style="left:248px;top:198px;width:44px;height:6px;font-size:3.6px;line-height:6px">OPERATION</div>
  <div class="tag" style="left:307px;top:198px;width:34px;height:6px;font-size:3.6px;line-height:6px">SUPPORT</div>
  <div class="a" style="left:198px;top:215px;font-size:4px;font-weight:700;color:var(--orange)">TOLMI</div>
  <div class="a p" style="left:220px;top:214px;font-size:2.1px;color:var(--muted);border-left:.3px solid var(--muted);padding-left:1.5px;line-height:1.3">Official System<br>Partner</div>
  <div class="a" style="left:246px;top:215px;font-size:4px;font-weight:700;color:var(--orange)">OBRU</div>
  <div class="a p" style="left:266px;top:216px;font-size:2.1px;color:var(--ink)">Go beyond CAD/CAM</div>
  <div class="a" style="left:305px;top:213px;font-size:4px;font-weight:700;color:#c41e1e">HOLLIN</div>
  <div class="a p" style="left:305px;top:218.5px;font-size:2px;color:var(--ink)">Automation Technology</div>
  <div class="foot"><div class="brand"><i></i>BRIMTEL</div></div>
</section>

</body>
</html>
```